Illustrationen für Familien-, Erziehungsberatung und Jugendberatung
Zielgruppe
Familien-, Erziehungsberatung und Jugendberatung in Frankfurt von 14 Erziehungsberatungsstellen
Zielgruppe: Eltern, Kinder und Jugendliche
Wir beraten bei familiären Krisen, Fragen zur Entwicklung und Erziehung, Beziehungsproblemen etc.
Aufgabenstellung
ansprechende Illustration für Familien (Eltern, Kinder und Jugendliche), diversitäts- und kultursensibel, inklusiv
das Bild oben auf der Flyervorderseite (siehe pdf) soll ersetzt werden, da zu stereotyp

```html
<!DOCTYPE html>
<html lang="de">
<head>
<meta charset="utf-8">
<title>Beratung für Eltern, Kinder und Jugendliche</title>
<link href="https://fonts.googleapis.com/css2?family=Carlito:wght@400;700&display=swap" rel="stylesheet">
<style>
  :root {
    --orange: #ee933a;
    --orange-light: #f3a858;
    --green: #b6c92b;
    --brown: #5a3f1f;
    --cream: #fdfcfa;
    --sky: #e4d9d0;
    --skyline: #a9a6ad;
    --skyline-blue: #93a7c0;
    --ground: #ece4dc;
    --badge-text: #f8eadc;
  }
  * { margin: 0; padding: 0; box-sizing: border-box; }
  html, body { width: 1200px; height: 2533px; overflow: hidden; background: var(--cream); }
  body { font-family: "Carlito", "Calibri", sans-serif; position: relative; }
  .flyer { position: relative; width: 1200px; height: 2533px; background: var(--cream); overflow: hidden; }
  .bar-top { position: absolute; left: 0; top: 0; width: 100%; height: 24px; background: var(--orange); }
  .hero-illustration {
    position: absolute; left: 0; top: 24px; width: 100%; height: 866px;
    background:
      radial-gradient(ellipse 60% 22% at 30% 60%, rgba(214,140,110,0.35), transparent 70%),
      radial-gradient(ellipse 55% 22% at 72% 58%, rgba(120,150,190,0.30), transparent 70%),
      radial-gradient(ellipse 45% 16% at 40% 78%, rgba(160,90,60,0.22), transparent 70%),
      linear-gradient(180deg, var(--sky) 0%, var(--skyline-blue) 20%, var(--skyline) 32%, var(--ground) 40%, var(--ground) 100%);
  }
  .rule-orange { position: absolute; left: 0; top: 890px; width: 100%; height: 4px; background: var(--orange); }
  .band-green { position: absolute; left: 0; top: 911px; width: 100%; height: 22px; background: var(--green); }
  .badge {
    position: absolute; left: 639px; top: 854px; width: 546px; height: 546px; border-radius: 50%;
    background: radial-gradient(circle at 50% 45%, var(--orange) 0%, #e48a35 100%);
    border: 8px solid var(--orange-light);
    color: var(--badge-text); text-align: center;
  }
  .badge-number { position: absolute; top: 40px; width: 100%; font-size: 140px; font-weight: 700; color: #fff; line-height: 1; }
  .badge-text { position: absolute; top: 165px; width: 100%; font-size: 58px; line-height: 70px; font-weight: 700; white-space: nowrap; }
  .headline {
    position: absolute; left: 113px; top: 1100px; font-size: 89px; line-height: 100px;
    font-weight: 700; color: var(--brown);
  }
  .subline {
    position: absolute; left: 113px; top: 1495px; font-size: 82px; line-height: 102px;
    font-weight: 700; color: var(--orange);
  }
  .info-label { position: absolute; left: 113px; top: 1798px; font-size: 56px; font-weight: 700; color: var(--brown); }
  .url-band {
    position: absolute; left: 0; top: 1887px; width: 100%; height: 160px; background: var(--orange);
    display: flex; align-items: center; justify-content: center;
    color: #fff; font-size: 104px; font-weight: 700; letter-spacing: 3px;
  }
  .brand { position: absolute; left: 90px; top: 2180px; display: flex; align-items: center; gap: 50px; }
  .brand-mark { width: 140px; height: 140px; border-radius: 50%; background: var(--orange-light); }
  .brand-name { font-size: 54px; line-height: 52px; font-weight: 700; color: var(--orange-light); }
  .bar-bottom { position: absolute; left: 0; top: 2483px; width: 100%; height: 50px; background: var(--green); }
</style>
</head>
<body>
<main class="flyer">
  <div class="bar-top"></div>
  <div class="hero-illustration" role="img" aria-label="Illustration: vielfältige, inklusive Gruppe aus Familien, Eltern, Kindern und Jugendlichen verschiedener Herkunft, darunter eine Person im Rollstuhl, vor der Frankfurter Skyline"></div>
  <div class="rule-orange"></div>
  <div class="band-green"></div>

  <h1 class="headline">Beratung für<br>Eltern, Kinder<br>und Jugendliche</h1>

  <div class="badge">
    <div class="badge-number">14</div>
    <div class="badge-text">Erziehungs- und<br>Familienberatungs-<br>stellen in Frankfurt<br>am Main</div>
  </div>

  <p class="subline">durch pädagogische und<br>psychologische Fachkräfte</p>

  <p class="info-label">Für nähere Informationen:</p>
  <div class="url-band">www.kifa-main.de</div>

  <div class="brand">
    <div class="brand-mark"></div>
    <div class="brand-name">Beratungsnetz<br>Mainstadt</div>
  </div>

  <div class="bar-bottom"></div>
</main>
</body>
</html>
```